Sports & fitness accessories website needs web design

We have a prestashop website that needs an appropriate skin that will work on the site and translate onto tarvik and qolm shops.
The site is currently live www.dolbrane.co.uk
Target Market(s)
Sports & fitness enthusiasts
Industry/Entity Type
Fitness
Number of Pages Required
5+ page
Font styles to use
Sans Serif

```html
<!DOCTYPE html>
<html lang="en">
<head>
<meta charset="utf-8">
<title>Vantora – Fitness Accessories</title>
<link rel="stylesheet" href="https://fonts.googleapis.com/css2?family=Lato:wght@400;700;900&family=Roboto:wght@500;700&family=Great+Vibes&display=swap">
<style>
:root{
  --orange:#f7941d;
  --orange-dark:#e07a0b;
  --black:#0d0d0d;
  --dark:#2b2b2b;
  --footer:#333333;
  --page:#f2f1ee;
  --white:#ffffff;
  --text:#333333;
  --border:#c9c9c9;
}
*{margin:0;padding:0;box-sizing:border-box}
html,body{width:971px;height:1200px;overflow:hidden}
body{font-family:'Lato',sans-serif;color:var(--text);background:var(--page);position:relative}
.abs{position:absolute}

/* top bar */
.topbar{left:0;top:0;width:971px;height:30px;background:var(--orange-dark)}
.topbar-phone{left:107px;top:0;height:30px;display:flex;align-items:center;gap:8px;color:var(--white);font-weight:700;font-size:12px}
.top-menu{left:510px;top:0;height:30px;display:flex}
.top-menu span{display:flex;align-items:center;justify-content:center;gap:8px;height:30px;background:#ececec;color:var(--dark);font-size:12px;font-weight:700;border-right:1px solid #c4c4c4}
.top-menu span.signin{background:#f4b266;border:none}
.caret{display:inline-block;width:0;height:0;border-left:4px solid transparent;border-right:4px solid transparent;border-top:5px solid var(--dark)}

/* header */
.header{left:0;top:30px;width:971px;height:79px;background:var(--black)}
.logo{left:107px;top:52px;color:var(--orange);font-weight:900;font-size:30px;line-height:30px;letter-spacing:1px}
.search{left:656px;top:41px;width:210px;height:24px;display:flex}
.search .field{flex:1;background:#d6d6d6;border-radius:3px 0 0 3px;color:#777;font-style:italic;font-size:11px;padding:6px 9px}
.search .go{width:33px;background:#2e2e2e;border-radius:0 3px 3px 0;display:flex;align-items:center;justify-content:center}
.cart{left:656px;top:75px;width:210px;height:24px;background:#2e2e2e;border-radius:3px;display:flex;align-items:center;gap:7px;padding:0 9px;color:#e8e8e8;font-size:11px}
.cart .caret{border-top-color:#e8e8e8;margin-left:auto}

/* hero */
.hero{left:0;top:109px;width:971px;height:241px;background:#dfe0e3}
.hero-photo{left:0;top:109px;width:440px;height:241px;background:linear-gradient(90deg,#8a8580 0%,#b9b6b1 45%,#dfe0e3 100%)}
.hero-text{left:480px;top:185px;width:420px;text-align:center;font-family:'Great Vibes',cursive;font-size:38px;line-height:45px;color:#1a1a1a}
.dots{left:667px;top:290px;display:flex;gap:4px}
.dots i{width:9px;height:9px;border-radius:50%;background:#fff;border:1px solid #9a9a9a}
.dots i.on{background:#2e7d32;box-shadow:inset 0 0 0 2px #fff}

/* nav */
.nav{left:0;top:350px;width:971px;height:31px;background:linear-gradient(#f9a43a,var(--orange-dark))}
.nav ul{position:absolute;left:107px;top:0;display:flex;list-style:none;height:31px}
.nav li{display:flex;align-items:center;color:var(--white);font-weight:700;font-size:12px;padding:0 22px;border-right:1px solid #d9720a}
.nav li:last-child{border:none}
.nav li.active{background:#f2f2f2;color:var(--dark);padding:0 19px}

/* tabs + products */
.tabs{left:107px;top:410px;display:flex;height:27px}
.tabs span{display:flex;align-items:center;justify-content:center;font-family:'Roboto',sans-serif;font-weight:700;font-size:16px}
.tabs .on{width:134px;background:var(--orange);color:var(--white);position:relative}
.tabs .on:after{content:"";position:absolute;left:62px;bottom:-5px;border-left:5px solid transparent;border-right:5px solid transparent;border-top:5px solid var(--orange)}
.tabs .off{width:126px;background:#e4e4e4;color:var(--dark)}
.panel{left:107px;top:437px;width:569px;height:495px;background:var(--white)}
.card{width:164px;height:201px;border:1px dashed var(--border);padding:5px;display:flex;flex-direction:column;align-items:center}
.card .img{width:152px;height:114px;border:1px solid #d4d4d4}
.card h3{font-weight:400;font-size:12px;line-height:14.5px;text-align:center;height:38px;display:flex;align-items:center;color:#3a3a3a}
.card .btns{display:flex;width:152px;height:30px;margin-top:2px}
.card .more{flex:1;background:linear-gradient(#f7f7f7,#cfcfcf);font-weight:700;font-size:12px;display:flex;align-items:center;justify-content:center;color:#222}
.card .buy{width:44px;background:var(--black);display:flex;align-items:center;justify-content:center}
.pager{left:107px;top:906px;width:569px;height:26px;background:var(--orange);display:flex;justify-content:center;align-items:center}
.pager span{color:var(--white);font-weight:700;font-size:15px;width:20px;text-align:center}
.pager span.cur{background:#efefef;color:#333;width:27px;height:26px;line-height:26px;margin:0 4px}

/* sidebar */
.info{left:698px;width:168px;background:var(--white);text-align:center;box-shadow:0 1px 2px rgba(0,0,0,.08)}
.info .badge{position:absolute;left:52px;top:-26px;width:64px;height:64px;border-radius:50%;background:var(--white);display:flex;justify-content:center;padding-top:12px}
.info h4{position:relative;font-weight:400;font-size:14px;margin-top:13px;color:#222}
.info p{position:relative;font-size:10px;line-height:13.5px;color:#333;padding:2px 8px 0}
.info p.nowrap{white-space:nowrap;font-size:9.5px;padding:2px 2px 0}
.promo{left:698px;top:744px;width:168px;height:188px;background:var(--black);color:var(--white);text-align:center;font-size:9.5px;line-height:13px;padding:0 9px}
.promo .mark{color:var(--orange);font-weight:900;font-size:17px;margin-top:8px;line-height:20px}
.promo p{margin-top:16px}

/* newsletter */
.news{left:0;top:964px;width:971px;height:52px;background:linear-gradient(#e9e8e5,#f6f5f3)}
.news .title{left:107px;top:9px;display:flex;align-items:center;gap:10px;font-size:20px;color:#2a2a2a}
.news .ring{width:35px;height:35px;border-radius:50%;border:2px solid var(--orange);display:flex;align-items:center;justify-content:center}
.news .chev{left:356px;top:10px}
.news .label{left:409px;top:20px;font-size:12px;color:#222}
.news .email{left:599px;top:15px;width:198px;height:23px;background:var(--white);border:1px solid #ddd;font-size:11px;color:#444;padding:4px 8px}
.news .submit{left:804px;top:15px;width:61px;height:22px;background:var(--orange);color:var(--white);font-weight:700;font-size:10.5px;display:flex;align-items:center;justify-content:center}

/* footer */
.footer{left:0;top:1016px;width:971px;height:154px;background:var(--footer);color:#e6e6e6}
.footer h5{position:absolute;top:19px;font-size:12px;font-weight:700;color:var(--white)}
.footer ul{position:absolute;top:44px;list-style:none;font-size:8.5px;line-height:16.4px}
.footer ul.wide{line-height:22.6px;top:40px}
.store{left:702px;top:1058px;width:163px;font-size:10.5px;color:#e6e6e6}
.store div{display:flex;align-items:center;gap:10px;height:38.5px;border-bottom:1px solid #555}
.store div:last-child{border:none}
.store div:first-child{height:30px;margin-top:-10px}
.bottombar{left:0;top:1170px;width:971px;height:30px;background:var(--black)}
.bottombar .copy{left:107px;top:9px;color:var(--white);font-weight:700;font-size:10.5px}
.social{left:758px;top:1176px;display:flex;gap:11px}
.social i{width:18px;height:18px;border-radius:3px}
</style>
</head>
<body>

<div class="abs topbar"></div>
<div class="abs topbar-phone">
  <svg width="18" height="18" viewBox="0 0 18 18"><circle cx="9" cy="9" r="8" fill="none" stroke="#fff" stroke-width="1.5"/><path d="M6 5.2l1.5-.5 1 2.2-1 .8c.4 1 1.2 1.9 2.2 2.3l.8-1 2.2 1-.5 1.5c-3 .4-6.4-3-6.2-6.3z" fill="#fff"/></svg>
  07700 900 418
</div>
<nav class="abs top-menu">
  <span style="width:86px">Contact Us</span>
  <span style="width:78px">English <i class="caret"></i></span>
  <span style="width:122px">Currency : GBP <i class="caret"></i></span>
  <span class="signin" style="width:69px">Sign in</span>
</nav>

<header class="abs header"></header>
<div class="abs logo">Vantora</div>
<div class="abs search"><div class="field">Search here...</div><div class="go"><svg width="14" height="14" viewBox="0 0 14 14"><circle cx="5.5" cy="5.5" r="4.3" fill="none" stroke="#fff" stroke-width="2"/><path d="M8.7 8.7L13 13" stroke="#fff" stroke-width="2.2"/></svg></div></div>
<div class="abs cart">
  <svg width="16" height="13" viewBox="0 0 16 13"><path d="M0 1h3l2 8h8l2-6H4" fill="none" stroke="#f7941d" stroke-width="1.5"/><circle cx="6" cy="11.5" r="1.2" fill="#f7941d"/><circle cx="12" cy="11.5" r="1.2" fill="#f7941d"/></svg>
  Cart (empty) <i class="caret"></i>
</div>

<section class="abs hero"></section>
<div class="abs hero-photo" role="img" aria-label="Smiling woman lifting dumbbells in a gym"></div>
<div class="abs hero-text">Lorem ipsum dolor sit amet consectetuer</div>
<div class="abs dots"><i></i><i></i><i class="on"></i><i></i></div>

<nav class="abs nav">
  <ul>
    <li class="active">Gym Accessories</li>
    <li>Fitness Accessories</li>
    <li>Weights</li>
    <li>Yoga</li>
    <li>Swimming</li>
    <li>Training</li>
    <li>Footwear</li>
    <li>Sale</li>
  </ul>
</nav>

<div class="abs tabs"><span class="on">Popular</span><span class="off">Best Sellers</span></div>
<main class="abs panel"></main>

<div class="abs card" style="left:122px;top:454px"><div class="img" role="img" aria-label="Foot wearing a cushioned arch support" style="background:radial-gradient(circle at 55% 55%,#c99a86,#f4ece8 60%,#fff 75%)"></div><h3>Archlo Pro Cushioned<br>Arch Supports</h3><div class="btns"><span class="more">More Detail</span><span class="buy"><svg width="16" height="13" viewBox="0 0 16 13"><path d="M0 1h3l2 8h8l2-6H4" fill="none" stroke="#f7941d" stroke-width="1.6"/><circle cx="6" cy="11.5" r="1.2" fill="#f7941d"/><circle cx="12" cy="11.5" r="1.2" fill="#f7941d"/></svg></span></div></div>
<div class="abs card" style="left:310px;top:454px"><div class="img" role="img" aria-label="White body tape measure" style="background:radial-gradient(circle at 50% 50%,#e2e2e2,#fff 65%)"></div><h3>Tapelo - Body Tape<br>Measure</h3><div class="btns"><span class="more">More Detail</span><span class="buy"><svg width="16" height="13" viewBox="0 0 16 13"><path d="M0 1h3l2 8h8l2-6H4" fill="none" stroke="#f7941d" stroke-width="1.6"/><circle cx="6" cy="11.5" r="1.2" fill="#f7941d"/><circle cx="12" cy="11.5" r="1.2" fill="#f7941d"/></svg></span></div></div>
<div class="abs card" style="left:497px;top:454px"><div class="img" role="img" aria-label="Row of colourful fitness tracker wristbands" style="background:linear-gradient(90deg,#fff 8%,#444 18%,#5a5a5a 32%,#1a9a8a 48%,#2f6fb5 64%,#6a4fb0 80%,#fff 92%)"></div><h3>Random Fitness<br>Accessories</h3><div class="btns"><span class="more">More Detail</span><span class="buy"><svg width="16" height="13" viewBox="0 0 16 13"><path d="M0 1h3l2 8h8l2-6H4" fill="none" stroke="#f7941d" stroke-width="1.6"/><circle cx="6" cy="11.5" r="1.2" fill="#f7941d"/><circle cx="12" cy="11.5" r="1.2" fill="#f7941d"/></svg></span></div></div>
<div class="abs card" style="left:122px;top:673px"><div class="img" role="img" aria-label="Pair of black hex dumbbells" style="background:radial-gradient(circle at 50% 50%,#2a2a2a,#888 40%,#fff 62%)"></div><h3>Fitness Accessory - Bouncor<br>8' Trampoli</h3><div class="btns"><span class="more">More Detail</span><span class="buy"><svg width="16" height="13" viewBox="0 0 16 13"><path d="M0 1h3l2 8h8l2-6H4" fill="none" stroke="#f7941d" stroke-width="1.6"/><circle cx="6" cy="11.5" r="1.2" fill="#f7941d"/><circle cx="12" cy="11.5" r="1.2" fill="#f7941d"/></svg></span></div></div>
<div class="abs card" style="left:310px;top:673px"><div class="img" role="img" aria-label="Resistance bands with foam handles" style="background:radial-gradient(circle at 50% 50%,#3b4a6a,#9aa3b5 40%,#fff 65%)"></div><h3>Core Motion<br>Accessories</h3><div class="btns"><span class="more">More Detail</span><span class="buy"><svg width="16" height="13" viewBox="0 0 16 13"><path d="M0 1h3l2 8h8l2-6H4" fill="none" stroke="#f7941d" stroke-width="1.6"/><circle cx="6" cy="11.5" r="1.2" fill="#f7941d"/><circle cx="12" cy="11.5" r="1.2" fill="#f7941d"/></svg></span></div></div>
<div class="abs card" style="left:497px;top:673px"><div class="img" role="img" aria-label="Blue swim mask and snorkel" style="background:radial-gradient(ellipse at 50% 50%,#2a4fa8,#9fb3dd 38%,#fff 62%)"></div><h3>Marlow Glide Mask And<br>Snorkel Set</h3><div class="btns"><span class="more">More Detail</span><span class="buy"><svg width="16" height="13" viewBox="0 0 16 13"><path d="M0 1h3l2 8h8l2-6H4" fill="none" stroke="#f7941d" stroke-width="1.6"/><circle cx="6" cy="11.5" r="1.2" fill="#f7941d"/><circle cx="12" cy="11.5" r="1.2" fill="#f7941d"/></svg></span></div></div>

<div class="abs pager">
  <svg width="10" height="12" viewBox="0 0 10 12" style="margin-right:12px"><path d="M8 0v12L0 6z" fill="#fff"/></svg>
  <span class="cur">1</span><span>2</span><span>3</span><span>4</span>
  <svg width="10" height="12" viewBox="0 0 10 12" style="margin-left:10px"><path d="M2 0v12l8-6z" fill="#fff"/></svg>
</div>

<aside>
  <div class="abs info" style="top:437px;height:85px">
    <div class="badge"><svg width="26" height="18" viewBox="0 0 26 18"><rect x="0" y="2" width="15" height="11" rx="1" fill="#f7941d"/><path d="M16 5h5l4 4v4h-9z" fill="#f7941d"/><circle cx="5" cy="15" r="2.5" fill="#f7941d" stroke="#fff"/><circle cx="20" cy="15" r="2.5" fill="#f7941d" stroke="#fff"/></svg></div>
    <h4>Delivery</h4><p>We dispatch orders worldwide from our state of the art UK distribution centre</p>
  </div>
  <div class="abs info" style="top:560px;height:60px">
    <div class="badge"><svg width="24" height="24" viewBox="0 0 24 24"><circle cx="12" cy="12" r="10.5" fill="none" stroke="#f7941d" stroke-width="2"/><path d="M8 7l2-.7 1.3 3-1.3 1c.5 1.3 1.6 2.5 2.9 3l1-1.3 3 1.3-.7 2C12 16 7.7 11.5 8 7z" fill="#f7941d"/></svg></div>
    <h4>Call Us</h4><p class="nowrap">You can call us on <b>+44 7700 900 418</b></p>
  </div>
  <div class="abs info" style="top:658px;height:73px">
    <div class="badge"><svg width="28" height="20" viewBox="0 0 28 20"><rect x="1" y="1" width="26" height="18" rx="3" fill="none" stroke="#f7941d" stroke-width="2"/><rect x="1" y="6" width="26" height="3" fill="#f7941d"/></svg></div>
    <h4>Secure Payments</h4><p>Payments can be made by<br>Debit or Credit cards &amp; Paqora</p>
  </div>
  <div class="abs promo">
    <div class="mark">Vantora</div>
    <p>Choose Vantora equipment to help improve your Strength, Speed and Agility or simply to enhance your overall fitness. Reach your performance goals with Vantora.</p>
    <p style="margin-top:10px">Vantora is a UK supplier of quality equipment at great value prices from a website you can trust.</p>
  </div>
</aside>

<section class="abs news">
  <div class="abs title"><span class="ring"><svg width="18" height="13" viewBox="0 0 18 13"><rect x="0" y="0" width="18" height="13" rx="1" fill="#f7941d"/><path d="M0 1l9 6 9-6" fill="none" stroke="#fff" stroke-width="1.4"/></svg></span>Newsletter Signup</div>
  <svg class="abs chev" width="36" height="34" viewBox="0 0 36 34"><path d="M2 2l14 15L2 32M16 2l14 15-14 15" fill="none" stroke="#d9d6d0" stroke-width="6"/></svg>
  <div class="abs label">Signup For Free Email Updates</div>
  <div class="abs email">Enter your email here</div>
  <div class="abs submit">SUBMIT</div>
</section>

<footer class="abs footer">
  <h5 style="left:109px">Categories</h5>
  <ul style="left:109px"><li>&gt; Women</li><li>&gt; Yoga</li><li>&gt; Endurance</li><li>&gt; Gym Accessories</li><li>&gt; Fitness Accessories</li><li>&gt; Weights</li></ul>
  <ul style="left:210px"><li>&gt; Swimming</li><li>&gt; Training</li><li>&gt; Footwear</li><li>&gt; Clearance</li><li>&gt; Sale</li></ul>
  <h5 style="left:332px">Information</h5>
  <ul style="left:330px"><li>&gt; Specials</li><li>&gt; New products</li><li>&gt; Best sellers</li><li>&gt; Contact us</li><li>&gt; Delivery</li><li>&gt; Legal Notice</li></ul>
  <ul style="left:409px"><li>&gt; Terms and conditions</li><li>&gt; Privacy Policy</li><li>&gt; Returns</li><li>&gt; Sitemap</li></ul>
  <h5 style="left:562px">My account</h5>
  <ul class="wide" style="left:562px"><li>&gt; My orders</li><li>&gt; My credit slips</li><li>&gt; My addresses</li><li>&gt; My personal info</li></ul>
  <h5 style="left:702px">Store Information</h5>
</footer>
<div class="abs store">
  <div><svg width="11" height="14" viewBox="0 0 11 14"><path d="M5.5 0a5 5 0 015 5c0 3.5-5 9-5 9S.5 8.5.5 5a5 5 0 015-5z" fill="#fff"/><circle cx="5.5" cy="5" r="2" fill="#333"/></svg>Vantora</div>
  <div><svg width="12" height="12" viewBox="0 0 12 12"><path d="M1 1.5L3.5.5l1.6 3-1.3 1.2c.7 1.4 1.8 2.6 3.2 3.3l1.2-1.3 3 1.6-1 2.5C5.2 11 1 6.8 1 1.5z" fill="#fff"/></svg>Call us now: 07700 900 418</div>
  <div><svg width="13" height="9" viewBox="0 0 13 9"><rect width="13" height="9" fill="#fff"/><path d="M0 0l6.5 5L13 0" fill="none" stroke="#333"/></svg>Email: support@vantora.co.uk</div>
</div>

<div class="abs bottombar"><div class="abs copy">© 2015 Vantora. All Rights Reserved.</div></div>
<div class="abs social">
  <i style="background:#3b5998"></i><i style="background:#29a9e1"></i><i style="background:#0077b5"></i><i style="background:#f7941d"></i>
</div>

</body>
</html>
```